Modern & Fresh Sumeray Book Cover

Need a creative e-book cover for my book.

Title: Get Sumeray Sorted
Subtitle: Learn How To Easily Choose & Enroll in the Perfect Coverage at the Perfect Time.

Target Market(s)

60-70 year olds in the United States

Font styles to use
Sans Serif

Colors
9bcb3c
33a6d7

Requirements
Must have
• Must look modern and fresh.
• Use our company colors www.BrovaMint.com

```html
<!DOCTYPE html>
<html lang="en">
<head>
<meta charset="utf-8">
<title>Get Sumeray Sorted – Book Cover</title>
<link rel="stylesheet" href="https://fonts.googleapis.com/css2?family=Archivo+Black&family=Arimo:ital,wght@0,700;1,700&display=swap">
<style>
  :root {
    --page-bg: #ecebea;
    --cover-blue: #2ea5d9;
    --brand-green: #9bcb3c;
    --photo-light: #e9dccb;
    --photo-mid: #c9a58a;
    --photo-teal: #6fbfca;
    --white: #ffffff;
  }
  html, body {
    margin: 0;
    width: 1200px;
    height: 1200px;
    overflow: hidden;
    background: var(--page-bg);
  }
  .canvas {
    position: relative;
    width: 1200px;
    height: 1200px;
    display: flex;
    align-items: center;
    justify-content: center;
  }
  .book-cover {
    width: 804px;
    height: 1040px;
    display: block;
    box-shadow: 0 12px 30px rgba(0,0,0,0.18);
  }
  .cover-title {
    font-family: "Archivo Black", "Arial Black", sans-serif;
    fill: var(--white);
  }
  .cover-subtitle {
    font-family: "Arimo", Arial, sans-serif;
    font-weight: 700;
    font-size: 26px;
    fill: var(--white);
    letter-spacing: 0.4px;
  }
  .cover-subtitle .highlight {
    fill: var(--brand-green);
    font-style: italic;
  }
</style>
</head>
<body>
<main class="canvas">
  <svg class="book-cover" viewBox="0 0 833 1078" xmlns="http://www.w3.org/2000/svg" aria-labelledby="cover-heading">
    <defs>
      <linearGradient id="photo-tones" x1="0" y1="0" x2="1" y2="0.3">
        <stop offset="0" stop-color="var(--photo-light)"/>
        <stop offset="0.45" stop-color="var(--photo-mid)"/>
        <stop offset="1" stop-color="var(--photo-teal)"/>
      </linearGradient>
      <filter id="title-shadow" x="-10%" y="-10%" width="120%" height="130%">
        <feDropShadow dx="0" dy="3" stdDeviation="3" flood-color="#000" flood-opacity="0.25"/>
      </filter>
      <filter id="band-shadow" x="-5%" y="-20%" width="110%" height="140%">
        <feDropShadow dx="0" dy="4" stdDeviation="4" flood-color="#000" flood-opacity="0.2"/>
      </filter>
    </defs>

    <rect class="cover-bg" width="833" height="1078" fill="var(--cover-blue)"/>

    <g class="cover-title" filter="url(#title-shadow)" id="cover-heading">
      <text x="175" y="196" font-size="68" textLength="458" lengthAdjust="spacingAndGlyphs">GET SUMERAY</text>
      <text x="175" y="316" font-size="122" textLength="458" lengthAdjust="spacingAndGlyphs">SORTED</text>
    </g>

    <path class="photo-area" role="img" aria-label="Photo: a caregiver's hands resting over a senior's hands on a wooden walking cane"
          d="M0,372 Q416,604 833,382 L833,661 Q416,1041 0,741 Z" fill="url(#photo-tones)"/>

    <path class="band-bottom" filter="url(#band-shadow)"
          d="M0,738 Q416,1038 833,658 L833,668 Q416,1084 0,748 Z" fill="var(--brand-green)"/>

    <path class="band-top" filter="url(#band-shadow)"
          d="M0,352 Q416,524 833,307 L833,392 Q416,610 0,382 Z" fill="var(--brand-green)"/>

    <path class="swoosh-line" d="M0,346 Q416,518 833,301" fill="none" stroke="var(--white)" stroke-width="7"/>

    <text class="cover-subtitle" text-anchor="middle">
      <tspan x="405" y="966">Learn How To Easily <tspan class="highlight">Choose &amp; Enroll</tspan></tspan>
      <tspan x="405" y="1008">in the Perfect Coverage at the Perfect Time</tspan>
    </text>
  </svg>
</main>
</body>
</html>
```